Business Card Design for ClearPathVitality

We need the new logo on a business card for 3 employees:
Nora Kettering, PhD, Advanced Instructor and Practitioner of SomaLink Integral Medicine (email: nora@clearpathvitality.com)
Ray Holm, Business Manager (email: ray@clearpathvitality.com)
Bea Marlowe, Administrative Assistant (email: bea@helixsense.com)

Target Market(s)

healthcare professionals

Industry/Entity Type

Alternative Medicine

Contact Information for Business Card

Names, titles, emails (names, titles, emails are in project description), phone, address, website, with logo and tagline. See below for address, phone, website: 418 Alder Ln, Bldg 12, Ste 305
Santa Cruz, CA 95060
831-555-2746
www.clearpathvitality.com
Tagline: Roots of Balance, Light of Renewal

Font styles to use
Other font styles liked:
• Gabriela

Colors
00a990
86cfc6
6b449b
b7a5cd
85abd2
abd036

Requirements
Must have
• Colors and style that match the logo design - shades such as blue, green, purple
• Compatible or same font as in the logo
Nice to have
• Nice if it goes with the theme of Nora's last business card - uploaded below
Should not have
• colors or style in conflict with the logo

```html
<!DOCTYPE html>
<html lang="en">
<head>
<meta charset="utf-8">
<title>ClearPathVitality – Business Card</title>
<link rel="stylesheet" href="https://fonts.googleapis.com/css2?family=Marcellus&family=Open+Sans:wght@400&display=swap">
<style>
  :root {
    --page-bg: #ece9e4;
    --card-bg: #ffffff;
    --brand-purple: #3d2a7d;
    --brand-green: #3bb54a;
    --wave-deep: #2f93d6;
    --wave-mid: #7cc3ec;
    --wave-light: #e3f2fb;
    --card-shadow: rgba(40, 30, 20, 0.18);
  }
  * { box-sizing: border-box; margin: 0; padding: 0; }
  html, body { width: 1200px; height: 800px; overflow: hidden; }
  body {
    background: var(--page-bg);
    font-family: "Open Sans", Arial, sans-serif;
    position: relative;
  }
  .card {
    position: absolute;
    top: 250px;
    width: 525px;
    height: 300px;
    background: var(--card-bg);
    box-shadow: 0 6px 18px var(--card-shadow);
    overflow: hidden;
  }
  .card--front { left: 50px; }
  .card--back { left: 625px; }

  .wave-band {
    position: absolute;
    inset: 0;
    width: 100%;
    height: 100%;
  }

  .brand {
    position: absolute;
    display: flex;
    align-items: center;
  }
  .brand__dot {
    border-radius: 50%;
    background: var(--brand-green);
    flex: none;
  }
  .brand__name {
    font-family: "Marcellus", Georgia, serif;
    color: var(--brand-purple);
    white-space: nowrap;
  }
  .card--front .brand { left: 28px; top: 42px; gap: 14px; }
  .card--front .brand__dot { width: 64px; height: 64px; }
  .card--front .brand__name { font-size: 27px; }

  .card--back .brand {
    left: 0; right: 0; top: 0; bottom: 0;
    justify-content: center;
    gap: 20px;
  }
  .card--back .brand__dot { width: 104px; height: 104px; }
  .card--back .brand__name { font-size: 38px; }

  .contact {
    position: absolute;
    color: var(--brand-purple);
    font-size: 17px;
    line-height: 1.25;
  }
  .contact--person { left: 28px; bottom: 28px; }
  .contact--reach { right: 26px; top: 112px; text-align: right; }
</style>
</head>
<body>

  <section class="card card--front" aria-label="Business card front">
    <svg class="wave-band" viewBox="0 0 525 300" preserveAspectRatio="none" role="img" aria-label="Soft flowing blue wave band sweeping across the card">
      <defs>
        <linearGradient id="waveFill" x1="0" y1="1" x2="1" y2="0">
          <stop offset="0" stop-color="var(--wave-light)"/>
          <stop offset="0.35" stop-color="var(--wave-mid)"/>
          <stop offset="0.65" stop-color="var(--wave-deep)"/>
          <stop offset="1" stop-color="var(--wave-light)"/>
        </linearGradient>
      </defs>
      <path d="M0 230 C 120 200, 200 250, 300 170 S 450 40, 525 30 L 525 110 C 440 110, 380 200, 290 240 S 100 260, 0 290 Z"
            fill="url(#waveFill)" opacity="0.85"/>
    </svg>

    <div class="brand">
      <span class="brand__dot"></span>
      <span class="brand__name">ClearPathVitality</span>
    </div>

    <div class="contact contact--reach">
      <p>Phone</p>
      <p>Email</p>
      <p>Website</p>
    </div>

    <div class="contact contact--person">
      <p>Name</p>
      <p>Address</p>
    </div>
  </section>

  <section class="card card--back" aria-label="Business card back">
    <div class="brand">
      <span class="brand__dot"></span>
      <span class="brand__name">ClearPathVitality</span>
    </div>
  </section>

</body>
</html>
```